Dietary supplement, Clean and simple.

Hi,
I’d like to talk about the project,

About us:
We are a dietary supplement (Vitamins, Minerals, amino acids etc.) company.
The goal is to have about 25 products at the end of this year. However, for this goal to be achieved we need a good label design to make our products represent our company values.
I’ll be here every day supporting your questions, we are fully committed to making the highest/best quality/customer experience possible.

About the design and our values:
- Professional (We are in the industry of professionalism and expertise. I would love to show we are competent at this, Id. Like to have the labels looks like we have done our research.)
- Efficient (White spacing, good use of the space available.)
- Simple (Straight forward, in 5 seconds they have to know what the product they have is/how functions. We’re trying to simplify it for the consumer.
- No distractions (the only visually “distracting” factor can be the vector art.)

The guidelines:
The goal is to have a universal design, with one element that changes (Vector art). I’ll attach a file/multiple files I think can show some visuals on what I’m looking for, and what parts of the design I think are good/bad.

Label size: 69x155mm (Front is 77.5mm)

Design whatever you think fits our image. You’re the design expert, all I care about is that it fits our company standards/image.

Use this color/font.
Font: Sans Serif
Main company color is Mind green #237D62 (Use this color for something in the design.)

What I thought would be cool/might looks ugly, who knows:
1. The front of the label: Should have 1 vector art, preferably in the top right corner. (That looks good in multiple colors. The vector can have multiple areas to color, I would prefer 2 main colors in the vector art. The interchangeable colors are used for multiple kinds of products.)
2. Text/product information on the left. The text that will have to be displayed:
- Product name for instance “Magnesium + B6”
- Description for the product for instance “Magnesium with ginger taste”
- Company name or logo. (Add ® behind it. We are soon to be trademark registered.)
3. We need to show the "daily intake" amount on the front and also the amount in the complete bottle. For instance, “Daily intake 1 capsule, 60 capsules”.
• You don’t have to design the backside of the label. After I chose a design, I’d like to chat and give specific information on what areas need to be assigned where. (Too complex because of the law.)
Updates

Hi, Please make the deadline 31 days total. I want designers to have the time to design. And not be rushed to finish it.

I want to extend the deadline because i feel like a slightly more medical look would be interesting. Hope you can come up with something!!

Target Market(s)

Dietary supplement consumers

Industry/Entity Type

Dietary supplements

Font styles to use
Sans Serif

Colors

Designer to choose colors to be used in the design.

Requirements
Must have
• Trademark icon "®" has to be at the top right after the company logo(text of logo)/name.

```html
<!DOCTYPE html>
<html lang="en">
<head>
<meta charset="utf-8">
<title>Linden Vale – Magnesium + B6 Label</title>
<link rel="stylesheet" href="https://fonts.googleapis.com/css2?family=Montserrat:wght@400;500;700&display=swap">
<style>
  :root {
    --bg: #ffffff;
    --ink: #111111;
    --brand-green: #1d5e2c;
    --mind-green: #237d62;
    --wave-gold: #f3e3c2;
  }
  * { margin: 0; padding: 0; box-sizing: border-box; }
  html, body {
    width: 1200px;
    height: 1200px;
    overflow: hidden;
    background: var(--bg);
  }
  .label {
    position: relative;
    width: 1200px;
    height: 1200px;
    font-family: "Montserrat", sans-serif;
    color: var(--ink);
  }
  .wave-art {
    position: absolute;
    left: 628px;
    top: 372px;
    width: 272px;
    height: 203px;
    background: radial-gradient(ellipse at 40% 45%, var(--wave-gold) 0%, rgba(243,227,194,0.55) 45%, rgba(255,255,255,0) 75%);
  }
  .brand {
    position: absolute;
    left: 361px;
    top: 508px;
    width: 265px;
    text-align: center;
    font-weight: 700;
    font-size: 28px;
    letter-spacing: 1px;
    color: var(--brand-green);
    white-space: nowrap;
  }
  .brand sup {
    font-size: 12px;
    vertical-align: top;
    position: relative;
    top: -2px;
    margin-left: 2px;
  }
  .product-name {
    position: absolute;
    left: 361px;
    top: 630px;
    width: 265px;
    text-align: center;
    font-weight: 700;
    font-size: 32px;
    line-height: 1;
    white-space: nowrap;
  }
  .product-desc {
    position: absolute;
    left: 361px;
    top: 680px;
    width: 265px;
    text-align: center;
    font-weight: 500;
    font-size: 19px;
    line-height: 1.2;
    white-space: nowrap;
    padding-bottom: 4px;
    border-bottom: 2px solid var(--mind-green);
  }
  .dosage {
    position: absolute;
    right: 574px;
    top: 793px;
    text-align: right;
    font-weight: 500;
    font-size: 15.5px;
    line-height: 23px;
    white-space: nowrap;
  }
  .dosage .count {
    display: flex;
    align-items: center;
    justify-content: flex-end;
    gap: 8px;
  }
  .capsule-icon { width: 30px; height: 11px; display: block; }
</style>
</head>
<body>
  <div class="label">
    <div class="wave-art" role="img" aria-label="Soft flowing golden line-wave vector art"></div>

    <div class="brand">Linden Vale<sup>®</sup></div>

    <h1 class="product-name">Magnesium + B6</h1>
    <p class="product-desc">Magnesium with ginger taste</p>

    <div class="dosage">
      <div class="intake">Daily intake: 1 capsule</div>
      <div class="count">
        <svg class="capsule-icon" viewBox="0 0 30 11" aria-hidden="true">
          <rect x="0.75" y="0.75" width="28.5" height="9.5" rx="4.75" fill="none" stroke="#111" stroke-width="1.3"/>
          <line x1="15" y1="0.75" x2="15" y2="10.25" stroke="#111" stroke-width="1.3"/>
        </svg>
        <span>60 capsules</span>
      </div>
    </div>
  </div>
</body>
</html>
```